Basic Company webpage with the elements and colors of our Logo

Basic Home page with a few pages:
- Home,
- About US,
- Contact us
- Services

Target Market(s)

Business Customers (B2B)

Coding

Coded - Design and coding required

Number of Pages Required

5+ page

Requirements
Must have
• Professional, Clean, Simple High Tech, Contact should have a contact us dialog for sending messages to us
Nice to have
• Meet with us links for calendar access though MS Bookings

```html
<!DOCTYPE html>
<html lang="en">
<head>
<meta charset="utf-8">
<title>Vantage Technology – Managed IT Support</title>
<link rel="stylesheet" href="https://fonts.googleapis.com/css2?family=Poppins:wght@300;400;500;600;700;800&display=swap">
<style>
:root{
  --navy:#0f4a6e;
  --navy-deep:#0b3a5a;
  --orange:#f9ae35;
  --ink:#111418;
  --muted:#8a8f96;
  --panel:#efefef;
  --field:#efebe8;
  --footer:#23262f;
  --white:#ffffff;
}
*{margin:0;padding:0;box-sizing:border-box}
html,body{width:1200px;height:4101px;overflow:hidden}
body{position:relative;background:var(--white);font-family:"Poppins",sans-serif;color:var(--ink)}
.abs{position:absolute}

/* header */
.site-header{position:absolute;left:0;top:0;width:1200px;height:103px}
.brand{position:absolute;display:flex;align-items:center;gap:10px;font-weight:600;color:var(--navy);font-size:21px;letter-spacing:.5px}
.brand-dot{width:14px;height:14px;border-radius:50%;background:var(--orange)}
.site-header .brand{left:44px;top:40px}
.main-nav{position:absolute;left:341px;top:45px;display:flex;gap:44px;font-size:14px;font-weight:400}
.header-phone{position:absolute;left:825px;top:44px;display:flex;align-items:center;gap:9px;font-size:13px}
.btn-pill{display:inline-flex;align-items:center;justify-content:center;border-radius:30px;font-weight:600;color:var(--white)}
.header-cta{position:absolute;left:1003px;top:40px;width:121px;height:28px;background:var(--orange);font-size:10px}

/* hero */
.hero{position:absolute;left:0;top:103px;width:1200px;height:730px}
.hero-title{position:absolute;left:79px;top:150px;color:var(--white);font-size:57px;font-weight:600;line-height:68px}
.hero-text{position:absolute;left:81px;top:308px;width:590px;color:var(--white);font-size:18px;line-height:22px;font-weight:400}
.hero-actions{position:absolute;left:79px;top:406px;display:flex;gap:17px}
.hero-actions .btn-pill{height:44px;font-size:18px;font-weight:500}
.btn-navy{background:var(--navy);width:185px}
.btn-orange{background:var(--orange);width:185px}

/* about */
.about-visual{position:absolute;left:24px;top:967px;width:512px;height:512px;border-radius:50%;background:var(--orange)}
.about-visual .photo{position:absolute;left:21px;top:38px;width:470px;height:470px;border-radius:50%;background:radial-gradient(circle at 50% 55%,#1f8fe0 0%,#0d3c8a 45%,#081b45 80%)}
.section-title{font-weight:600;font-size:38px;color:var(--ink)}
.about-title{position:absolute;left:619px;top:990px}
.about-text{position:absolute;left:619px;top:1061px;width:490px;font-size:15px;line-height:24.5px;color:var(--muted)}
.feature{position:absolute;left:613px;display:flex;gap:12px}
.feature-icon{width:66px;height:66px;border-radius:50%;background:var(--navy);flex:none}
.feature h3{font-size:15px;font-weight:500;margin-top:4px}
.feature p{font-size:10.5px;line-height:15px;color:var(--muted);width:230px}

/* services */
.services{position:absolute;left:8px;top:1584px;width:1186px;height:1066px;background:var(--panel)}
.services-title{position:absolute;left:0;width:1186px;top:114px;text-align:center}
.services-sub{position:absolute;left:0;width:1186px;top:180px;text-align:center;font-size:16px;color:#555}
.service-card{position:absolute;width:291px;height:303px;background:var(--white);border-radius:44px;text-align:center}
.service-icon{width:96px;height:92px;margin:28px auto 0;border-radius:18px;background:linear-gradient(160deg,#dfe9f1,#c9d9e6)}
.service-card h3{font-size:21px;font-weight:500;line-height:26px;margin-top:12px;color:var(--ink)}
.service-card p{font-size:14px;line-height:20.5px;color:var(--muted);margin:8px auto 0;width:255px}
.service-go{position:absolute;left:125px;bottom:-20px;width:41px;height:41px;border-radius:50%;background:var(--orange)}
.service-go svg{position:absolute;left:11px;top:10px}

/* stats */
.stats{position:absolute;left:8px;top:2659px;width:1186px;height:211px;background:linear-gradient(120deg,#0c4a7c,#0f3f6a 50%,#0c4675)}
.stat{position:absolute;top:45px;width:260px;text-align:center;color:var(--white)}
.stat-num{font-size:66px;font-weight:700;color:var(--orange);line-height:76px}
.stat-num sup{font-size:30px;vertical-align:32px}
.stat-label{font-size:19px;font-weight:500;margin-top:0}

/* appointment */
.appointment{position:absolute;left:124px;top:2977px;width:919px;height:481px;border:1px solid #e4e4e4;border-radius:22px}
.appointment-title{position:absolute;left:0;width:919px;top:42px;text-align:center;font-size:38px}
.field{position:absolute;background:var(--field);font-size:16px;color:#6b6b6b;padding:0 20px;display:flex;align-items:center}
.field.area{align-items:flex-start;padding-top:15px}
.submit{position:absolute;left:56px;top:395px;width:786px;height:60px;background:var(--navy);color:var(--white);font-size:19px;font-weight:500;display:flex;align-items:center;justify-content:center;border-radius:3px}

/* footer */
.site-footer{position:absolute;left:0;top:3566px;width:1200px;height:465px;background:var(--footer);color:var(--white)}
.site-footer .brand{left:84px;top:135px;color:var(--white);font-size:22px}
.footer-about{position:absolute;left:78px;top:208px;width:310px;font-size:16.5px;line-height:22.5px}
.footer-col{position:absolute;top:106px}
.footer-col h4{font-size:25px;font-weight:500;margin-bottom:21px}
.footer-col li{list-style:none;display:flex;align-items:center;gap:10px;font-size:16.5px;height:34px}
.arrow{width:20px;height:10px;flex:none}
.bottom-bar{position:absolute;left:0;top:4031px;width:1200px;height:70px}
.copyright{position:absolute;left:70px;top:24px;font-size:16px;color:#555}
.socials{position:absolute;left:976px;top:26px;display:flex;gap:32px}
.socials span{width:16px;height:16px;border-radius:50%;background:var(--orange)}
</style>
</head>
<body>

<header class="site-header">
  <div class="brand"><span class="brand-dot"></span>VANTAGE TECHNOLOGY</div>
  <nav class="main-nav"><span>HOME</span><span>ABOUT US</span><span>SERVICES</span><span>CONTACT</span></nav>
  <div class="header-phone">
    <svg width="20" height="20" viewBox="0 0 24 24"><path fill="#0f4a6e" d="M6.6 10.8a15 15 0 0 0 6.6 6.6l2.2-2.2c.3-.3.7-.4 1-.2 1.1.4 2.3.6 3.6.6.6 0 1 .4 1 1V20c0 .6-.4 1-1 1A17 17 0 0 1 3 4c0-.6.4-1 1-1h3.5c.6 0 1 .4 1 1 0 1.3.2 2.5.6 3.6.1.3 0 .7-.2 1z"/></svg>
    (+00) 555 010 200
  </div>
  <div class="btn-pill header-cta">CONTACT US</div>
</header>

<section class="hero">
  <svg class="abs" style="left:0;top:0" width="1200" height="730" viewBox="0 0 1200 730">
    <defs>
      <linearGradient id="heroFill" x1="0" y1="0" x2="1" y2="1">
        <stop offset="0" stop-color="#221a3e"/>
        <stop offset=".45" stop-color="#3a2f6b"/>
        <stop offset="1" stop-color="#1a1830"/>
      </linearGradient>
    </defs>
    <path d="M8 0H1194V520C1110 640 870 725 560 725C330 725 140 680 8 600Z" fill="var(--orange)"/>
    <path role="img" aria-label="Photo of IT professionals working with a laptop in an office" d="M8 0H1194V480C1100 600 860 695 560 695C330 695 150 650 8 575Z" fill="url(#heroFill)"/>
  </svg>
  <h1 class="hero-title">We manage your IT<br>so you don't have to</h1>
  <p class="hero-text">Trusted by 100+ businesses across Hertfordshire, Essex, London and beyond. We deliver outstanding Managed IT Support, Cloud and Communications services.</p>
  <div class="hero-actions">
    <span class="btn-pill btn-navy">FIND OUT MORE</span>
    <span class="btn-pill btn-orange">GET A QUOTE</span>
  </div>
</section>

<section class="about">
  <div class="about-visual"><div class="photo" role="img" aria-label="Illustration of a hand over a glowing security shield on a digital network"></div></div>
  <h2 class="section-title about-title">ABOUT US</h2>
  <p class="about-text">We are an award winning IT support and strategic services company with over 10 years' experience of delivering exceptional service to small and medium sized organisations across all sectors.</p>
  <div class="feature" style="top:1193px"><div class="feature-icon" role="img" aria-label="Stopwatch icon"></div><div><h3>Fast Response Times</h3><p>Super fast service desk with an industry leading average wait time of under 13 seconds.</p></div></div>
  <div class="feature" style="top:1285px"><div class="feature-icon" role="img" aria-label="Award badge icon"></div><div><h3>Fully Accredited</h3><p>Certified Cloud Partner, ISO 27001 &amp; 9001 Accredited, Industry Managed Services and VoIP Silver Partner</p></div></div>
  <div class="feature" style="top:1375px"><div class="feature-icon" role="img" aria-label="Thumbs up icon"></div><div><h3>Years of Experience</h3><p>We've been in business for over 10 years and now support over 100+ customers</p></div></div>
</section>

<section class="services">
  <h2 class="section-title services-title">OUR SERVICES</h2>
  <p class="services-sub">We provide fully accredited Managed IT Support, Cloud and Communications solutions</p>

  <article class="service-card" style="left:99px;top:276px"><div class="service-icon" role="img" aria-label="Managed support icon"></div><h3>Managed IT<br>Support</h3><p>We manage your IT ensuring systems are monitored, supported and protected to enhance business growth</p><span class="service-go"><svg width="20" height="20" viewBox="0 0 20 20"><path d="M6 3l9 7-9 7z" fill="#fff"/></svg></span></article>
  <article class="service-card" style="left:442px;top:276px"><div class="service-icon" role="img" aria-label="Professional services icon"></div><h3>Professional<br>Services</h3><p>We manage your IT ensuring systems are monitored, supported and protected to enhance business growth</p><span class="service-go"><svg width="20" height="20" viewBox="0 0 20 20"><path d="M6 3l9 7-9 7z" fill="#fff"/></svg></span></article>
  <article class="service-card" style="left:783px;top:276px"><div class="service-icon" role="img" aria-label="Cyber security icon"></div><h3>Cyber<br>Security</h3><p>We manage your IT ensuring systems are monitored, supported and protected to enhance business growth</p><span class="service-go"><svg width="20" height="20" viewBox="0 0 20 20"><path d="M6 3l9 7-9 7z" fill="#fff"/></svg></span></article>

  <article class="service-card" style="left:99px;top:627px"><div class="service-icon" role="img" aria-label="Communications icon"></div><h3 style="margin-top:24px">Communications</h3><p style="margin-top:30px">We manage your IT ensuring systems are monitored, supported and protected to enhance business growth</p><span class="service-go"><svg width="20" height="20" viewBox="0 0 20 20"><path d="M6 3l9 7-9 7z" fill="#fff"/></svg></span></article>
  <article class="service-card" style="left:442px;top:627px"><div class="service-icon" role="img" aria-label="Cloud solutions icon"></div><h3>Cloud<br>Solutions</h3><p>We manage your IT ensuring systems are monitored, supported and protected to enhance business growth</p><span class="service-go"><svg width="20" height="20" viewBox="0 0 20 20"><path d="M6 3l9 7-9 7z" fill="#fff"/></svg></span></article>
  <article class="service-card" style="left:783px;top:627px"><div class="service-icon" role="img" aria-label="Intelligence icon"></div><h3 style="margin-top:24px">Intelligence</h3><p style="margin-top:30px">We manage your IT ensuring systems are monitored, supported and protected to enhance business growth</p><span class="service-go"><svg width="20" height="20" viewBox="0 0 20 20"><path d="M6 3l9 7-9 7z" fill="#fff"/></svg></span></article>
</section>

<section class="stats">
  <div class="stat" style="left:48px"><div class="stat-num">15<sup>+</sup></div><div class="stat-label">Years of Experience</div></div>
  <div class="stat" style="left:317px"><div class="stat-num">99<sup>%</sup></div><div class="stat-label">Customer Satisfaction</div></div>
  <div class="stat" style="left:620px"><div class="stat-num">200<sup>+</sup></div><div class="stat-label">Companies Served</div></div>
  <div class="stat" style="left:870px"><div class="stat-num">98<sup>%</sup></div><div class="stat-label">Success Rate</div></div>
</section>

<section class="appointment">
  <h2 class="section-title appointment-title">GET AN APPOINTMENT</h2>
  <div class="field" style="left:59px;top:116px;width:374px;height:47px">Your Name</div>
  <div class="field" style="left:473px;top:116px;width:374px;height:47px">Your Phone</div>
  <div class="field" style="left:59px;top:194px;width:374px;height:47px">Email Address</div>
  <div class="field" style="left:473px;top:194px;width:374px;height:47px">Select Service</div>
  <div class="field area" style="left:59px;top:267px;width:788px;height:99px">Additional Message</div>
  <div class="submit">GET AN APPOINTMENT NOW</div>
</section>

<footer class="site-footer">
  <div class="brand"><span class="brand-dot"></span>VANTAGE TECHNOLOGY</div>
  <p class="footer-about">We are an award winning IT support and strategic services company with over 10 years' experience of delivering exceptional service to businesses across all sectors.</p>
  <div class="footer-col" style="left:433px;top:103px"><h4>What We Do</h4><ul>
    <li><svg class="arrow" viewBox="0 0 20 10"><path d="M0 5h16M12 1l5 4-5 4" stroke="#f9ae35" stroke-width="2" fill="none"/></svg>Managed IT Support</li>
    <li><svg class="arrow" viewBox="0 0 20 10"><path d="M0 5h16M12 1l5 4-5 4" stroke="#f9ae35" stroke-width="2" fill="none"/></svg>Cloud Desktop</li>
    <li><svg class="arrow" viewBox="0 0 20 10"><path d="M0 5h16M12 1l5 4-5 4" stroke="#f9ae35" stroke-width="2" fill="none"/></svg>Telephone Systems</li>
    <li><svg class="arrow" viewBox="0 0 20 10"><path d="M0 5h16M12 1l5 4-5 4" stroke="#f9ae35" stroke-width="2" fill="none"/></svg>Office Suite</li>
    <li><svg class="arrow" viewBox="0 0 20 10"><path d="M0 5h16M12 1l5 4-5 4" stroke="#f9ae35" stroke-width="2" fill="none"/></svg>Professional Services</li>
    <li><svg class="arrow" viewBox="0 0 20 10"><path d="M0 5h16M12 1l5 4-5 4" stroke="#f9ae35" stroke-width="2" fill="none"/></svg>Cyber Security</li>
    <li><svg class="arrow" viewBox="0 0 20 10"><path d="M0 5h16M12 1l5 4-5 4" stroke="#f9ae35" stroke-width="2" fill="none"/></svg>Disaster Recovery</li>
  </ul></div>
  <div class="footer-col" style="left:697px;top:110px"><h4>Useful Links</h4><ul>
    <li><svg class="arrow" viewBox="0 0 20 10"><path d="M0 5h16M12 1l5 4-5 4" stroke="#f9ae35" stroke-width="2" fill="none"/></svg>About Us</li>
    <li><svg class="arrow" viewBox="0 0 20 10"><path d="M0 5h16M12 1l5 4-5 4" stroke="#f9ae35" stroke-width="2" fill="none"/></svg>Services</li>
    <li><svg class="arrow" viewBox="0 0 20 10"><path d="M0 5h16M12 1l5 4-5 4" stroke="#f9ae35" stroke-width="2" fill="none"/></svg>Help &amp; Support</li>
    <li><svg class="arrow" viewBox="0 0 20 10"><path d="M0 5h16M12 1l5 4-5 4" stroke="#f9ae35" stroke-width="2" fill="none"/></svg>Refer A Friend</li>
    <li><svg class="arrow" viewBox="0 0 20 10"><path d="M0 5h16M12 1l5 4-5 4" stroke="#f9ae35" stroke-width="2" fill="none"/></svg>Privacy Policy</li>
    <li><svg class="arrow" viewBox="0 0 20 10"><path d="M0 5h16M12 1l5 4-5 4" stroke="#f9ae35" stroke-width="2" fill="none"/></svg>Contact Us</li>
  </ul></div>
  <div class="footer-col" style="left:923px;top:110px"><h4>Locations</h4><ul>
    <li><svg class="arrow" viewBox="0 0 20 10"><path d="M0 5h16M12 1l5 4-5 4" stroke="#f9ae35" stroke-width="2" fill="none"/></svg>Hertford IT Support</li>
    <li><svg class="arrow" viewBox="0 0 20 10"><path d="M0 5h16M12 1l5 4-5 4" stroke="#f9ae35" stroke-width="2" fill="none"/></svg>Stevenage IT Support</li>
    <li><svg class="arrow" viewBox="0 0 20 10"><path d="M0 5h16M12 1l5 4-5 4" stroke="#f9ae35" stroke-width="2" fill="none"/></svg>St Albans IT Support</li>
    <li><svg class="arrow" viewBox="0 0 20 10"><path d="M0 5h16M12 1l5 4-5 4" stroke="#f9ae35" stroke-width="2" fill="none"/></svg>Watford IT Support</li>
    <li><svg class="arrow" viewBox="0 0 20 10"><path d="M0 5h16M12 1l5 4-5 4" stroke="#f9ae35" stroke-width="2" fill="none"/></svg>Ware IT Support</li>
    <li><svg class="arrow" viewBox="0 0 20 10"><path d="M0 5h16M12 1l5 4-5 4" stroke="#f9ae35" stroke-width="2" fill="none"/></svg>Cheshunt IT Support</li>
  </ul></div>
</footer>

<div class="bottom-bar">
  <p class="copyright">© Vantage Technology 2025 | Company Number: 1111111</p>
  <div class="socials"><span></span><span></span><span></span></div>
</div>

</body>
</html>
```